A New and modern Business Card for Tarvish Commerce Partners Ltd

New and modern Logo and Business Card Attached is the current logo/business card designCurrently the business is called "Tarvish & Co." or TCP Ltd for short. This is subject to change.This business specialises in Telecoms and Energy. We work with the major networks (QX, Z7, etc) and also offer Energy Products saving clients money off their energy bills.These are business to business services.The current design incorporates a Pheonix, indicating rebirth, starting something new.We would like to maintain the Phoenix element but a newer modern style.We love colours in the logo 3 max.The aim of this is to be ultra slick and modern. I envisage Tarvish & Co. on one side of the card with long descriptions on the other side.Side 1:TCP Ltd/Logo?Side 2:TCP Ltd/Logo/Graphic?Tarvish & Co.Name:Address:Phone:Email:The design is mostly flexible but must incorporate a Phoenix.For example "Tarvish & Co." with a block phoenix behind the text...up to you.

Industry/Entity Type

Telecommunications

Contact Information for Business Card

Tarvish & Co.
Address:
Name:
Phone:
Email:

Logo Text

Tarvish & Co.

Colors
33a6d7
0792cd
acd037
9bcb3c
f78f20
fece3e

Requirements
Must have
• Phoenix
• 3/4 colours max
• Blue representing Technology (wireless)
• Green for Eco Energy
• Orange for Phoenix
• White business card background
Should not have
• phoenix must not all be red/ orange fire, we are a technology service company and the phoenix colours must represent this. Fire is not representative of our company.

```html
<!DOCTYPE html>
<html lang="en">
<head>
<meta charset="utf-8">
<title>Tarvish Commerce Partners Ltd – Business Card</title>
<link href="https://fonts.googleapis.com/css2?family=Libre+Baskerville:wght@700&family=Roboto:wght@400;500;700&family=Dancing+Script:wght@500&display=swap" rel="stylesheet">
<style>
  :root {
    --stage: #e4e7ea;
    --card: #ffffff;
    --ink-dark: #2b2f33;
    --ink-body: #41464b;
    --tech-blue: #0792cd;
    --tech-blue-soft: rgba(51, 166, 215, 0.12);
    --eco-green: #9bcb3c;
    --phoenix-orange: #f78f20;
    --rule: #c9ced3;
  }
  * { margin: 0; padding: 0; box-sizing: border-box; }
  html, body { width: 1200px; height: 1200px; overflow: hidden; background: var(--stage); }
  .stage { position: relative; width: 1200px; height: 1200px; }

  .card {
    position: absolute; left: 150px; width: 900px; height: 460px;
    background: var(--card);
    overflow: hidden;
    box-shadow: 0 6px 24px rgba(0, 0, 0, 0.12);
  }
  .card--back { top: 120px; }
  .card--front { top: 620px; }

  .card__band {
    position: absolute; left: 0; bottom: 0; width: 100%; height: 10px;
    background: linear-gradient(90deg, var(--tech-blue) 0 50%, var(--eco-green) 50% 100%);
  }

  .emblem-fade {
    position: absolute;
    background: radial-gradient(ellipse at center, var(--tech-blue-soft), transparent 70%);
  }
  .card--back .emblem-fade { left: 0; top: 0; width: 460px; height: 460px; }
  .card--front .emblem-fade { right: 0; top: 0; width: 440px; height: 460px; }

  .back-mark { position: absolute; right: 90px; top: 170px; text-align: left; }
  .back-mark__name {
    font-family: "Libre Baskerville", serif; font-weight: 700;
    font-size: 84px; line-height: 1; color: var(--tech-blue); letter-spacing: 2px;
  }
  .back-mark__full {
    margin-top: 10px; font-family: "Roboto", sans-serif; font-weight: 700;
    font-size: 18px; letter-spacing: 1px; color: var(--eco-green); text-transform: uppercase;
  }

  .brand { position: absolute; left: 40px; top: 60px; width: 380px; text-align: center; }
  .brand__dot {
    width: 110px; height: 110px; border-radius: 50%;
    background: var(--phoenix-orange); margin: 0 auto 30px;
  }
  .brand__name {
    font-family: "Libre Baskerville", serif; font-weight: 700;
    font-size: 34px; line-height: 1.25; color: var(--tech-blue);
  }
  .brand__tagline {
    margin-top: 14px; font-family: "Dancing Script", cursive; font-weight: 500;
    font-size: 30px; color: var(--eco-green);
  }

  .divider { position: absolute; left: 450px; top: 60px; width: 1px; height: 340px; background: var(--rule); }

  .contact { position: absolute; left: 495px; top: 110px; color: var(--ink-body); font-family: "Roboto", sans-serif; }
  .contact__name { font-family: "Libre Baskerville", serif; font-weight: 700; font-size: 32px; color: var(--ink-dark); }
  .contact__role { color: var(--phoenix-orange); font-size: 21px; margin-top: 2px; margin-bottom: 16px; }
  .contact__line { font-size: 21px; line-height: 1.45; }
  .contact__rows { margin-top: 10px; }
  .contact__row { display: flex; align-items: center; gap: 14px; font-size: 21px; line-height: 1.5; }
  .contact__row svg { width: 20px; height: 20px; flex: none; }
</style>
</head>
<body>
<main class="stage">

  <section class="card card--back" aria-label="Card back">
    <div class="emblem-fade" role="img" aria-label="Faint phoenix emblem in the background"></div>
    <div class="back-mark">
      <div class="back-mark__name">TCP LTD</div>
      <div class="back-mark__full">Tarvish Commerce Partners Limited</div>
    </div>
    <div class="card__band"></div>
  </section>

  <section class="card card--front" aria-label="Card front">
    <div class="emblem-fade" role="img" aria-label="Faint phoenix emblem in the background"></div>

    <div class="brand">
      <div class="brand__dot"></div>
      <div class="brand__name">Tarvish Commerce<br>Partners Ltd</div>
      <div class="brand__tagline">Service and sales organisation</div>
    </div>

    <div class="divider"></div>

    <div class="contact">
      <div class="contact__name">Alan Corwen</div>
      <div class="contact__role">President</div>
      <div class="contact__line">418 Halden Street West</div>
      <div class="contact__line">Suite 210, Marlow Falls, OR 97341</div>
      <div class="contact__rows">
        <div class="contact__row">
          <svg viewBox="0 0 24 24" aria-hidden="true"><path fill="#0792cd" d="M6.6 10.8a15.1 15.1 0 0 0 6.6 6.6l2.2-2.2a1 1 0 0 1 1-.25 11.4 11.4 0 0 0 3.6.57 1 1 0 0 1 1 1V20a1 1 0 0 1-1 1A17 17 0 0 1 3 4a1 1 0 0 1 1-1h3.5a1 1 0 0 1 1 1c0 1.25.2 2.45.57 3.57a1 1 0 0 1-.25 1z"/></svg>
          <span>541.902.6617</span>
        </div>
        <div class="contact__row">
          <svg viewBox="0 0 24 24" aria-hidden="true"><rect x="2" y="5" width="20" height="14" rx="1" fill="#0792cd"/><path d="M2 6l10 7 10-7" fill="none" stroke="#ffffff" stroke-width="1.6"/></svg>
          <span>info@TarvishCommerce.com</span>
        </div>
      </div>
    </div>
    <div class="card__band"></div>
  </section>

</main>
</body>
</html>
```